Mobile Spray tanner needs a Mobile Spray tanning business card design

I need a simple but eye-catching business card design. I would like the business card to be in two colours only (Hot pink background with black Silhouette & black writing). I would like the white behind the silhouette removed and the other bits on the silhouette removed (to be just a black silhouette with a hot pink bikini on). I would like the black writing to be aesthetically pleasing and quite artistic, but easy to read). Thank you very much

```html
<!DOCTYPE html>
<html lang="en">
<head>
<meta charset="utf-8">
<title>Sunkissed Skin – Mobile Spray Tanning Business Card</title>
<link rel="stylesheet" href="https://fonts.googleapis.com/css2?family=PT+Serif:wght@700&display=swap">
<style>
  :root {
    --backdrop: #ece8e9;
    --card-pink: #c86b8c;
    --ink: #333033;
    --silhouette-dark: #141414;
    --bikini-pink: #c2457e;
  }
  * { margin: 0; padding: 0; box-sizing: border-box; }
  html, body {
    width: 1200px;
    height: 1000px;
    overflow: hidden;
    background: var(--backdrop);
  }
  .canvas {
    position: relative;
    width: 1200px;
    height: 1000px;
  }
  .business-card {
    position: absolute;
    left: 350px;
    top: 70px;
    width: 500px;
    height: 860px;
    background: var(--card-pink);
    box-shadow: 0 6px 18px rgba(0,0,0,0.18);
    font-family: "PT Serif", Georgia, serif;
    font-weight: 700;
    color: var(--ink);
  }
  .silhouette-figure {
    position: absolute;
    left: 130px;
    top: 50px;
    width: 250px;
    height: 430px;
    border-radius: 110px 110px 40px 40px;
    background: linear-gradient(180deg, var(--silhouette-dark) 0%, var(--silhouette-dark) 55%, var(--bikini-pink) 72%, var(--silhouette-dark) 85%);
  }
  .business-name {
    position: absolute;
    top: 505px;
    left: 0;
    width: 100%;
    text-align: center;
    font-size: 40px;
    letter-spacing: 1px;
  }
  .service-line {
    position: absolute;
    left: 0;
    width: 100%;
    text-align: center;
    font-size: 34px;
    letter-spacing: 1px;
  }
  .service-line.mobile { top: 568px; }
  .service-line.spray { top: 625px; }
  .contact-phone {
    position: absolute;
    top: 720px;
    left: 95px;
    display: flex;
    align-items: center;
    gap: 18px;
    font-size: 28px;
    letter-spacing: 1px;
  }
  .phone-icon { width: 26px; height: 48px; }
</style>
</head>
<body>
  <main class="canvas">
    <article class="business-card">
      <div class="silhouette-figure" role="img" aria-label="Black silhouette of a kneeling woman wearing a pink bikini"></div>
      <h1 class="business-name">SUNKISSED SKIN</h1>
      <p class="service-line mobile">MOBILE</p>
      <p class="service-line spray">SPRAY TANNING</p>
      <p class="contact-phone">
        <svg class="phone-icon" viewBox="0 0 26 48" aria-hidden="true">
          <rect x="2" y="2" width="22" height="44" rx="4" fill="none" stroke="var(--ink)" stroke-width="3"/>
          <line x1="2" y1="9" x2="24" y2="9" stroke="var(--ink)" stroke-width="2"/>
          <line x1="2" y1="38" x2="24" y2="38" stroke="var(--ink)" stroke-width="2"/>
          <circle cx="13" cy="42" r="1.8" fill="var(--ink)"/>
        </svg>
        <span>0491- 570- 156</span>
      </p>
    </article>
  </main>
</body>
</html>
```